BRASKET LAND SERVICES BILLBOARD DESIGN

I NEED A BILLBOARD FOR MY BUSINESS. WE ARE A LAND CLEARING COMPANY AND I WOULD LIKE TO ADD A PICTURE OF MY TRACK LOADER TO THE SIGN. OPEN TO COLORS. I WOULD ALSO LIKE TO HAVE MY PHONE NUMBER 555-284-6170, WEBSITE WWW.BRASKETLANDSERVICES.EXAMPLE, AND EMAIL ON THE SIGN (CONTACT@BRASKETLANDSERVICES.EXAMPLE). DESIGNERS CAN HAVE THE FREEDOM TO DO WHATEVER STYLE THEY WANT AND TO USE ANY COLORS THEY WANT.

Target Market(s)

ANYONE WITH PROPERTY

Requirements
Must have
• PICTURE OF TRACK LOADER, WEBSITE, PHONE NUMBER, EMAIL
Nice to have
• OPEN TO ANYTHING
Should not have
• OPEN TO ANYTHING

```html
<!DOCTYPE html>
<html lang="en">
<head>
<meta charset="utf-8">
<title>Brasket Land Services Billboard</title>
<link href="https://fonts.googleapis.com/css2?family=Oswald:wght@500;700&display=swap" rel="stylesheet">
<style>
  :root {
    --ink: #050505;
    --yellow: #f7e629;
    --white: #ffffff;
    --stage: #e9eaec;
    --photo-leaf: #4f5d2c;
    --photo-ground: #a8946a;
    --photo-machine: #e8562a;
  }
  html, body {
    margin: 0;
    width: 1200px;
    height: 1200px;
    overflow: hidden;
    background: var(--stage);
  }
  .billboard {
    position: absolute;
    left: 40px;
    top: 400px;
    width: 1120px;
    height: 400px;
    overflow: hidden;
    font-family: "Oswald", "Arial Narrow", sans-serif;
    box-shadow: 0 10px 30px rgba(0,0,0,0.25);
  }
  .loader-photo {
    position: absolute;
    inset: 0;
    background:
      radial-gradient(ellipse 30% 35% at 70% 55%, var(--photo-machine) 0%, rgba(232,86,42,0.35) 55%, transparent 100%),
      linear-gradient(180deg, #3d4a22 0%, var(--photo-leaf) 45%, #8c7d55 62%, var(--photo-ground) 100%);
  }
  .info-panel {
    position: absolute;
    inset: 0;
    background: var(--ink);
    clip-path: polygon(0 0, 500px 0, 440px 100%, 0 100%);
  }
  .brand-name {
    position: absolute;
    left: 28px;
    top: 48px;
    margin: 0;
    font-weight: 700;
    line-height: 0.98;
    text-transform: uppercase;
    letter-spacing: 0.5px;
  }
  .brand-name .first {
    display: block;
    color: var(--white);
    font-size: 58px;
  }
  .brand-name .second {
    display: block;
    color: var(--yellow);
    font-size: 62px;
  }
  .phone-band {
    position: absolute;
    left: 22px;
    top: 212px;
    width: 440px;
    height: 78px;
    background: var(--yellow);
    clip-path: polygon(0 12%, 100% 0, 94% 100%, 0 100%);
    display: flex;
    align-items: center;
    gap: 12px;
    padding-left: 18px;
    box-sizing: border-box;
  }
  .phone-band svg { width: 40px; height: 40px; flex: none; }
  .phone-number {
    color: var(--ink);
    font-weight: 700;
    font-size: 56px;
    line-height: 1;
    padding-top: 6px;
  }
  .contact-list {
    position: absolute;
    left: 36px;
    top: 312px;
    margin: 0;
    padding: 0;
    list-style: none;
    color: var(--white);
    font-weight: 500;
    font-size: 18px;
    letter-spacing: 0.2px;
  }
  .contact-list li {
    display: flex;
    align-items: center;
    gap: 10px;
    margin-bottom: 10px;
  }
  .contact-list svg { width: 18px; height: 18px; flex: none; }
</style>
</head>
<body>
  <section class="billboard">
    <div class="loader-photo" role="img" aria-label="Photo of an orange tracked loader with a forestry mulcher attachment on a grassy hillside in front of trees"></div>
    <div class="info-panel"></div>

    <h1 class="brand-name">
      <span class="first">BRASKET</span>
      <span class="second">LAND SERVICES</span>
    </h1>

    <div class="phone-band">
      <svg viewBox="0 0 40 40" aria-hidden="true">
        <path d="M9 6c2-1 4 0 5 2l3 6c1 2 0 3-1 4l-2 2c2 4 5 7 9 9l2-2c1-1 2-2 4-1l6 3c2 1 3 3 2 5l-2 3c-2 2-5 3-8 2C15 36 6 27 3 15c-1-3 0-6 2-8z" fill="#050505"/>
        <path d="M24 6a12 12 0 0 1 10 10M23 11a7 7 0 0 1 6 6" stroke="#050505" stroke-width="2.6" fill="none" stroke-linecap="round"/>
      </svg>
      <span class="phone-number">555-284-6170</span>
    </div>

    <ul class="contact-list">
      <li>
        <svg viewBox="0 0 20 20" aria-hidden="true"><g fill="none" stroke="#fff" stroke-width="1.4"><circle cx="10" cy="10" r="8.5"/><ellipse cx="10" cy="10" rx="3.8" ry="8.5"/><path d="M1.5 10h17M3 5.5h14M3 14.5h14"/></g></svg>
        WWW.BRASKETLANDSERVICES.EXAMPLE
      </li>
      <li>
        <svg viewBox="0 0 20 20" aria-hidden="true"><g fill="none" stroke="#fff" stroke-width="1.4"><rect x="2" y="5" width="16" height="12"/><path d="M2 5l8 7 8-7"/></g></svg>
        CONTACT@BRASKETLANDSERVICES.EXAMPLE
      </li>
    </ul>
  </section>
</body>
</html>
```